Trifold - Gentle Horizon Therapy

Marianne Dobbs, Psy.D.Licensed Psychologist

this is for hypnosis and meditation
I like decorative font for my name (conservative decorative)

calming effect is most imortant

Target Market(s)

clients with depression, pain, anxiety - adults and aged

Industry/Entity Type

Conservative

Font styles to use
Serif

Colors
abd037
85cae6
cadf82
34a7d7
ffffff
886aae
6b449b

Requirements
Must have
• I like zen-like calming effects. lime Green, light blues and purple. I like waves and color.
• I like water and light, flowers and plants - bamboo, stacking rocks, ocean, water, lotus flowers
Should not have
• not too much purple
• Mostly green and blue

```html
<!DOCTYPE html>
<html lang="en">
<head>
<meta charset="utf-8">
<title>Gentle Horizon Therapy – Trifold Inside</title>
<link rel="stylesheet" href="https://fonts.googleapis.com/css2?family=Oswald:wght@400;500&family=Arimo:wght@400;700&display=swap">
<style>
  :root {
    --blue-deep: #3589c6;
    --blue-mid: #3b95d0;
    --cyan: #34b3e6;
    --sky: #85cae6;
    --brand-blue: #34a7d7;
    --lime: #abd037;
    --lime-soft: #cadf82;
    --purple: #886aae;
    --purple-deep: #6b449b;
    --white: #ffffff;
    --ink: #1c1c1c;
  }
  * { box-sizing: border-box; margin: 0; padding: 0; }
  html, body { width: 1200px; height: 933px; overflow: hidden; background: var(--white); }
  .canvas {
    position: relative; width: 1200px; height: 933px; overflow: hidden;
    background: var(--white); font-family: "Arimo", Arial, sans-serif; color: var(--ink);
  }
  .hero-photo {
    position: absolute; left: 795px; top: 0; width: 405px; height: 200px;
    background:
      radial-gradient(circle at 62% 30%, rgba(255,255,240,.95) 0 9%, rgba(230,240,200,.6) 16%, transparent 30%),
      radial-gradient(circle at 85% 15%, rgba(255,250,210,.7), transparent 40%),
      linear-gradient(180deg, #b9cf6a 0%, #8fb03c 45%, #5e8a22 100%);
  }
  .shapes { position: absolute; inset: 0; width: 1200px; height: 933px; }
  .portrait {
    position: absolute; left: 37px; top: 648px; width: 176px; height: 226px;
    border-radius: 50% 50% 46% 46%;
    background: radial-gradient(ellipse at 50% 45%, #d7a777 0%, #c79266 35%, #b7d9de 70%, rgba(255,255,255,0) 78%);
  }
  .panel-title {
    position: absolute; left: 53px; top: 38px; width: 700px;
    font-family: "Oswald", "Arial Narrow", sans-serif; font-weight: 500;
    font-size: 28.5px; letter-spacing: .2px; color: var(--white); white-space: nowrap;
  }
  .col {
    position: absolute; font-size: 16px; line-height: 21.3px; color: var(--white);
  }
  .col p { text-align: justify; }
  .col-intro { left: 51px; top: 92px; width: 317px; }
  .col-intro .lead-end { text-align-last: justify; margin-bottom: 12px; }
  .col-session { left: 425px; top: 92px; width: 324px; }
  .col-session .subhead { text-align: left; }
  .col-session .clear-head { margin-top: 14px; text-align: left; }
  .benefits { list-style: none; margin-top: 2px; }
  .benefits li { position: relative; padding-left: 17px; }
  .benefits li::before {
    content: ""; position: absolute; left: 3px; top: 8px; width: 5px; height: 5px;
    border-radius: 50%; background: var(--white);
  }
  .about {
    position: absolute; left: 819px; top: 186px; width: 340px;
  }
  .about-title {
    font-family: "Oswald", "Arial Narrow", sans-serif; font-weight: 500;
    font-size: 29px; line-height: 39px; color: var(--purple); margin-bottom: 6px;
  }
  .about-text { font-size: 16px; line-height: 21.3px; }
  .conditions-head {
    margin-top: 18px; font-size: 15px; line-height: 20px; font-weight: 700; color: var(--purple);
  }
  .conditions { list-style: none; margin-top: 16px; font-size: 16px; line-height: 21.4px; }
  .conditions li { position: relative; padding-left: 18px; }
  .conditions li::before {
    content: ""; position: absolute; left: 2px; top: 8px; width: 5px; height: 5px;
    border-radius: 50%; background: var(--purple);
  }
  .bio { position: absolute; left: 229px; top: 653px; width: 572px; }
  .bio-name { font-size: 20px; font-weight: 700; color: var(--brand-blue); margin-bottom: 4px; }
  .bio-text { font-size: 13.3px; line-height: 18.8px; text-align: justify; }
</style>
</head>
<body>
<main class="canvas">
  <div class="hero-photo" role="img" aria-label="Photograph of a dandelion seed head in sunlit green grass"></div>

  <svg class="shapes" viewBox="0 0 1200 933" aria-hidden="true">
    <defs>
      <linearGradient id="panelFill" x1="0" y1="0" x2="0" y2="1">
        <stop offset="0" stop-color="#3a8fcb"/>
        <stop offset="1" stop-color="#3492cf"/>
      </linearGradient>
      <clipPath id="panelClip">
        <path d="M0 0 H795 V570 C650 560 470 590 300 615 C180 632 80 636 0 630 Z"/>
      </clipPath>
    </defs>
    <path d="M0 0 H795 V570 C650 560 470 590 300 615 C180 632 80 636 0 630 Z" fill="url(#panelFill)"/>
    <g clip-path="url(#panelClip)">
      <path d="M795 185 C775 330 690 470 500 560 C360 622 180 645 0 645 V933 H795 Z" fill="var(--cyan)"/>
    </g>
    <path d="M795 150 C900 110 1050 82 1200 92 V200 H795 Z" fill="var(--purple)"/>
    <path d="M795 196 C900 160 1050 128 1200 132 V933 H795 Z" fill="var(--white)"/>
  </svg>

  <h1 class="panel-title">CLEARING OLD STUFF AND MAKING WAY FOR NEW BEGINNINGS</h1>

  <section class="col col-intro">
    <p class="lead-end">If you have been unable to change how you feel, think or act, it is likely that you are being affected by experiences from your past. When something is painful or disturbing, it slams into awareness and leaves a lasting impression. Even when the experience is finished, deeper parts of the mind may continue to respond as if the disturbing event is still occurring. When fueled by the ongoing influence of past events, emotional problems, destructive behaviors and relationship</p>
    <p>difficulties are impossible to overcome. You may consciously understand the value of changing a behavior, but unless your deeper mind is transformed, change is not likely. In GHT the subconscious mind is engaged, and the influence of past events is eliminated. Energy that was blocked is released and healing takes place. Negative habits and painful emotions are replaced by feelings of well-being and motivation for desired action.</p>
  </section>

  <section class="col col-session">
    <p class="subhead">What happens in a GHT Session?</p>
    <p>Trauma is stored in the mind and body. In GHT, you will experience profound physiological calm and you will be guided towards emotional resolution in a gentle, creative and even humorous way. You access inner resources of light, wisdom and peace. You step into the awareness of your wise and true self. As Elena Marsh states: “we all have a beautiful light within, we just sometimes forget it is there”. From this place of light, emotional memories are easily reframed with new meaning. You will leave the session feeling peaceful and sourced from within by a free-flowing energy.</p>
    <p class="clear-head">Clear Your Mind and Change Your World</p>
    <ul class="benefits">
      <li>Discover and resolve subconscious causes for emotional and behavioral difficulties</li>
      <li>Eliminate unconscious conflicts blocking desired change</li>
      <li>Promote mind / body healing</li>
    </ul>
  </section>

  <section class="about">
    <h2 class="about-title">WHAT IS GENTLE<br>HORIZON THERAPY (GHT)</h2>
    <p class="about-text">GHT dramatically enhances mood, creates calm, eases grief, optimizes health and promotes success. It is a form of hypnosis that clears stuck patterns of thinking and feeling at the subconscious level. Past emotionally charged memories are cleared. You do not have to talk about problems, share scattered thoughts, cry nor re-experience uncomfortable emotions. You are guided to engage in deep brain processing to create an internal shift for automatic changes in thoughts, feelings and behaviors. Profound change happens within your nervous system facilitating lasting positive effects. Only one or two sessions are needed to experience immediate symptom relief.</p>
    <p class="conditions-head">GHT is effective for many of life’s<br>problems including:</p>
    <ul class="conditions">
      <li>PTSD, Sexual Abuse and Childhood Abuse</li>
      <li>Grief, Infidelity and Heartbreak</li>
      <li>Relationship issues</li>
      <li>Anger and Resentment</li>
      <li>Guilt / Shame</li>
      <li>Anxiety / Fear</li>
      <li>Nightmares / Insomnia</li>
      <li>Stress-related symptoms and Pain</li>
    </ul>
  </section>

  <div class="portrait" role="img" aria-label="Portrait photograph of Dr. Marianne Dobbs"></div>

  <section class="bio">
    <h3 class="bio-name">Dr. Marianne Dobbs</h3>
    <p class="bio-text">Dr. Dobbs is a licensed clinical psychologist specializing in adults and seniors. She treats people for depression, anxiety, grief, sexual trauma, PTSD, relationship issues, infidelity, divorce and stress-related symptoms. She has over 20 years of clinical experience in mental health and is an adjunct counseling professor at Westbrook University. She received her Master’s and Doctorate degrees in Clinical Psychology from Coral Bay University in Honolulu, Hawaii. She earned a Bachelor’s of Science degree in Rehabilitation Medicine from Lakeshore University in Kingston, Canada. At Stillwater Holistic Wellness Center, she provides initial evaluations, assessment, diagnosis and comprehensive treatment planning. She will collaborate with you to create solutions for healing, empowerment and wellness.</p>
  </section>
</main>
</body>
</html>
```